New Packaging and label for New Beard Oil and Shampoo brand from London

Oils, Shampoo ect .. Beard Oil Ingredients: Application Directions: Apply to beard by weight in a small amount of oil will naturally absorb. Leaving it soft & conditioned. Ingredients: Coconut oil, scented oil, Oud oil, vitamin E 100% Natural `i will have 5 types of oils Vanilla Oud Rose Oud Cocktail Tea tree Arabian Night

Target Market(s)

A fashionable well groomed professional gentleman who is willing to invest in his appearance.

Industry/Entity Type

It Company

Font styles to use
Sans Serif

Colors

Designer to choose colors to be used in the design.

Requirements
Must have
• Beard Oil Ingredients: Application Directions: Apply to a beard by a small amount of oil will naturally absorb. Leaving it soft & conditioned. Ingredients: Coconut Oil, Scented Oil, Oil Oud, Vitamin E 100% Natural 1.0z 30ml Made in Uk i will have 5 types of oils Vanilla Oud Rose Oud Cocktail Tea Tree Arabian Beard Night Shampoo APPLICATION DIRECTIONS Massage into the beard / hair and rinse out with warm water. Distorted shampoos, there are no nasty chemicals which are damaging your beard instead of the wheat proteins and oils that you add to the hair follicles with nutrients and naturally adding a protective coating. INGREDIENTS Aqua (Water), Capryl / caprylyl glucoside, Cocomidopropyl betaine, Glycerin (Veg), Xanthan gum, Phenoxyethanol, Hydrolysed wheat protein, Aloe barbadensis (Aloe vera) leaf powder, Sodium benzoate, Potassium sorbate1 3.4 oz, 100ml Cylinder packaging for the Oils, Box for the shampoo
Nice to have
• I want "London" written underneath the logo and oil name.

```html
<!DOCTYPE html>
<html lang="en">
<head>
<meta charset="utf-8">
<title>Thornbury Beard – Beard Oil Labels</title>
<link rel="stylesheet" href="https://fonts.googleapis.com/css2?family=Montserrat:wght@700&family=Quicksand:wght@400;500&display=swap">
<style>
  :root {
    --backdrop-top: #141414;
    --backdrop-bottom: #000000;
    --label-black: #111111;
    --label-edge: #1c1c1c;
    --ink-white: #f4f4f4;
    --ink-gold: #c9a24a;
  }
  * { box-sizing: border-box; margin: 0; padding: 0; }
  html, body { width: 1200px; height: 813px; overflow: hidden; }
  body {
    background: linear-gradient(180deg, var(--backdrop-top) 0%, var(--backdrop-bottom) 100%);
    font-family: "Quicksand", sans-serif;
  }
  .label-row {
    position: absolute;
    left: 60px;
    top: 270px;
    display: flex;
    gap: 24px;
  }
  .label {
    width: 192px;
    height: 272px;
    background: var(--label-black);
    border: 1px solid var(--label-edge);
    position: relative;
    color: var(--ink-white);
    text-align: center;
  }
  .brand-name {
    position: absolute;
    top: 50px;
    left: 0;
    right: 0;
    font-family: "Montserrat", sans-serif;
    font-weight: 700;
    font-size: 20px;
    line-height: 22px;
    letter-spacing: 0.5px;
    color: var(--ink-white);
    text-transform: uppercase;
  }
  .scent-name {
    position: absolute;
    top: 158px;
    left: 0;
    right: 0;
    font-size: 21px;
    font-weight: 400;
    color: var(--ink-white);
  }
  .origin {
    position: absolute;
    top: 187px;
    left: 0;
    right: 0;
    font-size: 14px;
    font-weight: 400;
    color: var(--ink-gold);
  }
  .volume {
    position: absolute;
    top: 246px;
    left: 0;
    right: 0;
    font-size: 13px;
    font-weight: 500;
    color: var(--ink-white);
  }
  .volume small { font-size: 9px; }
</style>
</head>
<body>
  <main class="label-row">
    <section class="label">
      <p class="brand-name">Thornbury<br>Beard</p>
      <h2 class="scent-name">Vanilla Oud</h2>
      <p class="origin">London</p>
      <p class="volume">1 oz <small>(30 ml)</small></p>
    </section>
    <section class="label">
      <p class="brand-name">Thornbury<br>Beard</p>
      <h2 class="scent-name">Rose Oud</h2>
      <p class="origin">London</p>
      <p class="volume">1 oz <small>(30 ml)</small></p>
    </section>
    <section class="label">
      <p class="brand-name">Thornbury<br>Beard</p>
      <h2 class="scent-name">Cocktail</h2>
      <p class="origin">London</p>
      <p class="volume">1 oz <small>(30 ml)</small></p>
    </section>
    <section class="label">
      <p class="brand-name">Thornbury<br>Beard</p>
      <h2 class="scent-name">Tea Tree</h2>
      <p class="origin">London</p>
      <p class="volume">1 oz <small>(30 ml)</small></p>
    </section>
    <section class="label">
      <p class="brand-name">Thornbury<br>Beard</p>
      <h2 class="scent-name">Arabian Night</h2>
      <p class="origin">London</p>
      <p class="volume">1 oz <small>(30 ml)</small></p>
    </section>
  </main>
</body>
</html>
```